A small boutique Accounting and Mortgage Broking firm needs a business card design

Quorvel is a Brisbane based boutique accounting and mortgage broking firm. We offer a range of extensive financial services like accounting, tax consulting, book-keeping and mortgage broking.
We need a business card that stands out. The content can stay as it is on the existing card unless you recommend us to change anything on it for a better design.
Please remove the mobile number and give us a suitable format to change the details like email address and name.
Industry/Entity Type
Business
Contact Information for Business Card
Dalian Okoruwe
Quorvel Group Pty Ltd
3/412 Brackwin Rd Tarrowby QLD 4196
PO Box 829 Tarrowby QLD 4196
T 07 3184 5526
F 07 3952 1087
E dokoruwe@quorvel.net.au
Accountants Tax Agents, Mortgage Brokers
www.quorvel.net.au
Look and feel
Each slider illustrates characteristics of the customer's brand and the style your logo design should communicate.

```html
<!DOCTYPE html>
<html lang="en">
<head>
<meta charset="utf-8">
<title>Quorvel Group — Business Card</title>
<link rel="stylesheet" href="https://fonts.googleapis.com/css2?family=Source+Sans+3:wght@400;600;700&display=swap">
<style>
  :root {
    --stage: #2b2b2b;
    --card: #1b1b1b;
    --card-edge: #2a2a2a;
    --green: #7ac143;
    --grey: #5a5a5a;
    --text: #e6e6e6;
    --rule: #333333;
  }
  * { margin: 0; padding: 0; box-sizing: border-box; }
  html, body {
    width: 1200px; height: 900px; overflow: hidden;
    background: var(--stage);
    font-family: "Source Sans 3", "Myriad Pro", sans-serif;
  }
  .stage {
    width: 1200px; height: 900px;
    display: flex; align-items: center; justify-content: center; gap: 40px;
  }
  .card {
    width: 540px; height: 320px;
    background: var(--card);
    border: 1px solid var(--card-edge);
    border-radius: 22px;
    position: relative;
    box-shadow: 0 12px 30px rgba(0,0,0,0.45);
  }
  /* Front */
  .card-front { display: flex; }
  .brand-panel {
    width: 250px; display: flex; flex-direction: column;
    align-items: center; justify-content: center; gap: 14px;
  }
  .brand-mark { display: flex; align-items: center; gap: 12px; }
  .brand-dot {
    width: 22px; height: 22px; border-radius: 50%;
    background: var(--green);
  }
  .brand-name {
    font-size: 40px; font-weight: 600; color: var(--grey); letter-spacing: 0.5px;
  }
  .tagline {
    font-size: 17px; color: var(--grey); letter-spacing: 1px; text-transform: uppercase;
  }
  .divider {
    width: 1px; background: var(--rule); margin: 70px 0;
  }
  .contact-panel {
    padding: 58px 0 0 22px; color: var(--text); font-size: 16px; line-height: 1.3;
  }
  .person-name { color: var(--green); font-size: 23px; font-weight: 600; margin-bottom: 8px; }
  .company { font-weight: 700; text-transform: uppercase; }
  .address { margin-bottom: 10px; }
  .contact-line .label { color: var(--green); margin-right: 4px; }
  /* Back */
  .card-back {
    display: flex; flex-direction: column; align-items: center; justify-content: center;
  }
  .card-back .brand-mark { margin-bottom: 12px; }
  .card-back .brand-name { font-size: 36px; }
  .card-back .tagline { font-size: 15px; margin-bottom: 22px; }
  .services { color: var(--green); font-size: 16px; margin-bottom: 12px; }
  .website { color: var(--green); font-size: 15px; }
</style>
</head>
<body>
<main class="stage">
  <section class="card card-front">
    <div class="brand-panel">
      <div class="brand-mark">
        <span class="brand-dot"></span>
        <span class="brand-name">Quorvel</span>
      </div>
      <p class="tagline">Care. Clarity. Progress.</p>
    </div>
    <div class="divider"></div>
    <div class="contact-panel">
      <p class="person-name">Dalian Okoruwe</p>
      <p class="company">Quorvel Group Pty Ltd</p>
      <p class="address">3/412 Brackwin Rd<br>Tarrowby QLD 4196<br>PO Box 829<br>Tarrowby QLD 4196</p>
      <p class="contact-line"><span class="label">T:</span>07 3184 5526</p>
      <p class="contact-line"><span class="label">F:</span>07 3952 1087</p>
      <p class="contact-line"><span class="label">E:</span>dokoruwe@quorvel.net.au</p>
    </div>
  </section>
  <section class="card card-back">
    <div class="brand-mark">
      <span class="brand-dot"></span>
      <span class="brand-name">Quorvel</span>
    </div>
    <p class="tagline">Care. Clarity. Progress.</p>
    <p class="services">Accountants | Tax Agents | Mortgage Brokers</p>
    <p class="website">www.quorvel.net.au</p>
  </section>
</main>
</body>
</html>
```